Online Psychology Practice needs business cards.

Online Psychology service needs business cards. Have own logo- please see uploaded. I have other file formats if you need (not sure one needed?)

Details for Business Card:
Fiona Kettlewood
Clinical Psychologist BPsych, BPsych (Hons), MPsych (Clin), MAPS
T: 0457260714 | F: 08 71526804
E: hello@harbourlightmindcarestudio.com.au
W: harbourlightmindcarestudio.com.au

Industry/Entity Type

Health

Contact Information for Business Card

Logo plus details above (couldn't write in this section)

```html
<!DOCTYPE html>
<html lang="en">
<head>
<meta charset="UTF-8">
<title>Harbourlight Mindcare Studio — Business Card</title>
<link href="https://fonts.googleapis.com/css2?family=Poppins:wght@300;400;500;700&display=swap" rel="stylesheet">
<style>
  :root {
    --page-bg: #ebebeb;
    --card-white: #ffffff;
    --navy: #1b5a84;
    --teal: #128ca9;
    --teal-mid: #15809f;
    --ink-on-dark: #ffffff;
    --brand-ink: #1b5e86;
  }
  * { box-sizing: border-box; margin: 0; padding: 0; }
  html, body {
    width: 1200px; height: 1000px; overflow: hidden;
    background: var(--page-bg);
    font-family: "Poppins", sans-serif;
  }
  .card {
    position: absolute; left: 222px; width: 755px; height: 432px;
    box-shadow: 0 14px 30px rgba(0,0,0,0.22);
    overflow: hidden;
  }
  /* Front */
  .card-front { top: 57px; background: var(--card-white); }
  .band {
    position: absolute; left: 0; width: 100%; height: 27px;
    background: linear-gradient(90deg, var(--navy) 0%, var(--teal-mid) 60%, var(--teal) 100%);
  }
  .band-top { top: 0; }
  .band-bottom { bottom: 0; }
  .front-brand {
    position: absolute; left: 0; top: 0; width: 100%; height: 100%;
    display: flex; flex-direction: column; align-items: center; justify-content: center;
    gap: 18px;
  }
  .brand-dot {
    width: 58px; height: 58px; border-radius: 50%;
    background: var(--brand-ink);
  }
  .brand-name {
    color: var(--brand-ink); font-weight: 500; text-align: center;
    font-size: 30px; line-height: 1.15; letter-spacing: 0.5px;
  }
  /* Back */
  .card-back {
    top: 511px;
    background: linear-gradient(225deg, var(--navy) 0%, var(--teal-mid) 30%, var(--teal) 55%, var(--teal) 100%);
    color: var(--ink-on-dark);
  }
  .rule { position: absolute; height: 1.5px; background: var(--ink-on-dark); }
  .rule-top { top: 23px; left: 0; width: 715px; }
  .rule-bottom { top: 410px; left: 41px; right: 0; }
  .person-name {
    position: absolute; left: 40px; top: 137px;
    font-size: 42px; font-weight: 700; letter-spacing: -0.5px; line-height: 1;
  }
  .credentials {
    position: absolute; left: 41px; top: 180px;
    font-size: 17px; font-weight: 300; line-height: 21px; text-transform: uppercase;
  }
  .contact {
    position: absolute; left: 41px;
    font-size: 18px; font-weight: 500; line-height: 1;
  }
  .contact b { font-weight: 700; margin-right: 4px; }
  .contact-web { top: 240px; }
  .contact-mail { top: 274px; }
  .contact-phones { top: 384px; }
  .contact-phones .gap { display: inline-block; width: 24px; }
  .back-brand {
    position: absolute; left: 588px; top: 300px; width: 140px;
    display: flex; flex-direction: column; align-items: center; gap: 8px;
  }
  .back-brand .brand-dot { width: 30px; height: 30px; background: var(--ink-on-dark); }
  .back-brand .brand-name { color: var(--ink-on-dark); font-size: 15px; }
</style>
</head>
<body>
  <section class="card card-front">
    <div class="band band-top"></div>
    <div class="front-brand">
      <span class="brand-dot"></span>
      <p class="brand-name">Harbourlight<br>Mindcare Studio</p>
    </div>
    <div class="band band-bottom"></div>
  </section>

  <section class="card card-back">
    <div class="rule rule-top"></div>
    <h1 class="person-name">FIONA KETTLEWOOD</h1>
    <p class="credentials">Clinical Psychologist BPsych,<br>BPsych (Hons), MPsych (Clin), MAPS</p>
    <p class="contact contact-web"><b>W:</b>harbourlightmindcarestudio.com.au</p>
    <p class="contact contact-mail"><b>E:</b>hello@harbourlightmindcarestudio.com.au</p>
    <p class="contact contact-phones"><b>T:</b>0457260714<span class="gap"></span><b>F:</b>08 71526804</p>
    <div class="back-brand">
      <span class="brand-dot"></span>
      <p class="brand-name">Harbourlight<br>Mindcare Studio</p>
    </div>
    <div class="rule rule-bottom"></div>
  </section>
</body>
</html>
```